Theme for 60th Anniversary party for a Business

We are looking for a theme for our 60th year party. The theme we used for our 50th party was a movie premier with a drive-in movie. Info on our 50th party is here http://brookwingaero.com/about/50th-anniversary/. The theme must incorporate what we do as a business. Full website at www.brookwingaero.com. The theme would be expanded upon with the use of props or other items to make a large celebration. The party would have around 400 invited guests to take place at our business location on an airport. Please provide details of your theme along with potential props, activities, or other items that would make your theme work. A logo for the theme will also be needed and could be provided with the theme.
Updates

Target Market(s)

Customers, Vendors, Potential Customers

Industry/Entity Type

Movie

Requirements
Must have
• Activities that can take place during event.

```html
<!DOCTYPE html>
<html lang="en">
<head>
<meta charset="utf-8">
<title>Passport Around the World – Theme Proposal</title>
<link rel="stylesheet" href="https://fonts.googleapis.com/css2?family=Cinzel:wght@700&family=Marcellus&family=Questrial&display=swap">
<style>
  :root {
    --navy-deep: #1a2544;
    --navy: #26315a;
    --navy-light: #2f3a66;
    --title-gold: #e7e3c6;
    --subtitle-cream: #f3efcf;
    --heading-yellow: #f4e45a;
    --body-white: #f6f6f2;
    --note-yellow: #f2e04a;
  }
  * { box-sizing: border-box; margin: 0; padding: 0; }
  html, body {
    width: 960px;
    height: 1200px;
    overflow: hidden;
    background: var(--navy-deep);
  }
  .proposal {
    position: relative;
    width: 960px;
    height: 1200px;
    overflow: hidden;
    background:
      radial-gradient(ellipse at 50% 40%, var(--navy-light) 0%, var(--navy) 55%, var(--navy-deep) 100%);
    color: var(--body-white);
    font-family: "Questrial", "Century Gothic", sans-serif;
    text-align: center;
  }
  .proposal__title {
    position: absolute;
    top: 30px;
    left: 0;
    width: 100%;
    font-family: "Cinzel", "Trajan Pro", serif;
    font-weight: 700;
    font-size: 98px;
    line-height: 1;
    letter-spacing: 2px;
    color: var(--title-gold);
    text-shadow: 0 2px 2px rgba(0, 0, 0, 0.45), 0 -1px 0 rgba(255, 255, 255, 0.25);
  }
  .proposal__subtitle {
    position: absolute;
    top: 146px;
    left: 0;
    width: 100%;
    font-family: "Marcellus", "Optima", serif;
    font-size: 36px;
    line-height: 1.2;
    color: var(--subtitle-cream);
  }
  .proposal__content {
    position: absolute;
    top: 218px;
    left: 0;
    width: 100%;
    font-size: 18px;
    line-height: 21px;
  }
  .section-heading {
    color: var(--heading-yellow);
  }
  .section-text {
    white-space: nowrap;
  }
  .gap { height: 21px; }
  .gap--double { height: 52px; }
  .gap--small { height: 20px; }
  .gap--footer { height: 25px; }
  .designer-note {
    color: var(--note-yellow);
    white-space: nowrap;
  }
</style>
</head>
<body>
<main class="proposal">
  <h1 class="proposal__title">PASSPORT</h1>
  <h2 class="proposal__subtitle">AROUND THE WORLD</h2>

  <div class="proposal__content">
    <section class="theme-section">
      <h3 class="section-heading">DRESS CODE OPTIONS:</h3>
      <p class="section-text">People can wear clothing representing any culture from around the globe.</p>
    </section>

    <div class="gap--double"></div>

    <section class="theme-section">
      <h3 class="section-heading">Invites:</h3>
      <p class="section-text">The invites could look like a passport, but with your modified logo on the front instead<br>
      of the United States crest that is on there now. It would also have the date and title at the<br>
      top saying “Celebrating 60 years by taking you around the world” or something<br>
      Catchy.</p>
    </section>

    <div class="gap--small"></div>

    <section class="theme-section">
      <h3 class="section-heading">Arrival:</h3>
      <p class="section-text">Set up a front ‘desk’ with ropes etc like an airport check in area. Have someone dress as<br>
      a receptionist that takes people’s passports (invites) and coats.</p>
    </section>

    <div class="gap--small"></div>

    <section class="theme-section">
      <h3 class="section-heading">Decor:</h3>
      <p class="section-text">Inside the party you could have themed areas representing a different country.<br>
      The bar could could be decorated to look like a jamaican theme with fake palm trees and the<br>
      bartender could dress jamaican with the hat and whig. Have island themed drinks.</p>
      <div class="gap"></div>
      <p class="section-text">You can have a whine bar that is Italian themed. The beer can be served at an<br>
      American themed bar.</p>
      <div class="gap"></div>
      <p class="section-text">Each table can have different artifacts, pictures, colors that represent a country/culture.</p>
      <div class="gap"></div>
      <p class="section-text">Serve Mexican, American, Italian etc....Have different foods on the menu from<br>
      around the globe.</p>
    </section>

    <div class="gap--small"></div>

    <section class="theme-section">
      <h3 class="section-heading">Activities:</h3>
      <p class="section-text">Have a dance floor and play different styles of music from different cultures throughout the night.</p>
      <div class="gap"></div>
      <p class="section-text">Around the world trivia, each table works as a team.</p>
      <div class="gap"></div>
      <p class="section-text">If possible, see if there are any entertainers that are popular in other cultures such as a mime,<br>
      magician, dancers, singers etc.....maybe even have an exotic animal person come and<br>
      let people see/hold reptiles/animals from other countries.</p>
      <div class="gap"></div>
      <p class="section-text">If there are some good artists around, have someone come and draw caricatures dressed<br>
      like they are in Venice.</p>
      <div class="gap"></div>
      <p class="section-text">Best Dressed contest.</p>
      <div class="gap"></div>
      <p class="section-text">Raffle off a couple cruises or trips!</p>
    </section>

    <div class="gap--footer"></div>

    <p class="designer-note">I can modify your logo as well as help design the invites if needed. I would just need a better logo<br>
    file than what is online. Thanks!</p>
  </div>
</main>
</body>
</html>
```